Varek services highend custom homes

We build high end custom homes and timber frames we specialize in rustic hand made designs along with iron and concrete accents to add a modern touch 90% of my homes are buit on lake front properries attached is my logo and slogan as of now and my previous one

Target Market(s)

High end custom homes

Industry/Entity Type

Custom residential construction

Contact Information for Business Card

Been in buissness 8+ years inssured and reliable

Colors
A7469A
B969AE
D3A5CF
EDDBEB
F8F0F9

Requirements
Must have
• Must have slogan and phone number
Should not have
• A combination of rustic yet modern accents

```html
<!DOCTYPE html>
<html lang="en">
<head>
<meta charset="utf-8">
<title>Varek Services – Business Cards</title>
<link rel="stylesheet" href="https://fonts.googleapis.com/css2?family=Jost:wght@400;500;700&display=swap">
<style>
  :root {
    --backdrop: #3a3a3a;
    --forest: #4b5a47;
    --paper: #ffffff;
    --stripe: #8c8c8c;
    --ink-light: #ffffff;
    --divider: rgba(255,255,255,0.35);
  }
  * { margin: 0; padding: 0; box-sizing: border-box; }
  html, body { width: 1200px; height: 1200px; overflow: hidden; }
  body {
    background: var(--backdrop);
    font-family: "Jost", sans-serif;
    display: flex;
    flex-direction: column;
    align-items: center;
    justify-content: center;
    gap: 60px;
  }
  .card {
    position: relative;
    width: 860px;
    height: 491px;
    border-radius: 40px;
    overflow: hidden;
  }

  /* Front card */
  .card-front { background: var(--paper); }
  .front-band {
    position: absolute;
    left: 0; right: 0; top: 278px; bottom: 0;
    background: var(--forest);
  }
  .front-stripe {
    position: absolute;
    left: 0; right: 0; top: 262px; height: 9px;
    background: var(--stripe);
  }
  .brand {
    position: absolute;
    display: flex;
    flex-direction: column;
    align-items: center;
  }
  .brand-row { display: flex; align-items: center; gap: 18px; }
  .brand-square { display: block; }
  .brand-name {
    font-weight: 700;
    text-transform: uppercase;
    letter-spacing: 0.02em;
    line-height: 1;
  }
  .brand-slogan {
    font-weight: 400;
    text-transform: uppercase;
    letter-spacing: 0.12em;
  }
  .card-front .brand { left: 0; right: 0; top: 70px; }
  .card-front .brand-square { width: 62px; height: 62px; background: var(--forest); }
  .card-front .brand-name { font-size: 62px; color: var(--forest); }
  .card-front .brand-slogan { font-size: 19px; color: var(--forest); margin-top: 16px; }

  .person {
    position: absolute;
    left: 62px; top: 345px;
    padding-left: 22px;
    border-left: 7px solid var(--ink-light);
    color: var(--ink-light);
  }
  .person-name { font-size: 40px; font-weight: 500; line-height: 1; }
  .person-role { font-size: 24px; font-weight: 400; margin-top: 4px; letter-spacing: 0.02em; }

  .front-divider {
    position: absolute;
    left: 478px; top: 300px;
    width: 1px; height: 120px;
    background: var(--divider);
  }
  .contact {
    position: absolute;
    left: 510px; top: 305px;
    list-style: none;
    color: var(--ink-light);
    font-size: 22px;
    line-height: 1.3;
  }
  .contact li { display: flex; align-items: flex-start; gap: 10px; }
  .contact svg { width: 20px; height: 20px; margin-top: 4px; flex: none; fill: var(--ink-light); }

  /* Back card */
  .card-back { background: var(--forest); }
  .card-back .brand { left: 0; right: 0; top: 0; bottom: 0; justify-content: center; }
  .card-back .brand-square { width: 80px; height: 80px; background: var(--ink-light); }
  .card-back .brand-name { font-size: 80px; color: var(--ink-light); }
  .card-back .brand-slogan { font-size: 24px; color: var(--ink-light); margin-top: 22px; }
</style>
</head>
<body>

  <section class="card card-front">
    <div class="front-stripe"></div>
    <div class="front-band"></div>

    <div class="brand">
      <div class="brand-row">
        <span class="brand-square"></span>
        <span class="brand-name">Varek Services</span>
      </div>
      <p class="brand-slogan">• From lodges to landmarks •</p>
    </div>

    <div class="person">
      <p class="person-name">JOHN DOE</p>
      <p class="person-role">POSITION</p>
    </div>

    <div class="front-divider"></div>

    <ul class="contact">
      <li>
        <svg viewBox="0 0 24 24" aria-hidden="true"><path d="M6.6 10.8a15.1 15.1 0 0 0 6.6 6.6l2.2-2.2a1 1 0 0 1 1-.25 11.4 11.4 0 0 0 3.6.57 1 1 0 0 1 1 1V20a1 1 0 0 1-1 1A17 17 0 0 1 3 4a1 1 0 0 1 1-1h3.5a1 1 0 0 1 1 1c0 1.25.2 2.45.57 3.57a1 1 0 0 1-.25 1z"/></svg>
        <span>(000) 000 0000</span>
      </li>
      <li>
        <svg viewBox="0 0 24 24" aria-hidden="true"><path d="M2 5h20v14H2z M4 7v.4l8 5.2 8-5.2V7z" fill-rule="evenodd"/></svg>
        <span>email@company.com</span>
      </li>
      <li>
        <svg viewBox="0 0 24 24" aria-hidden="true"><path d="M12 2a7 7 0 0 0-7 7c0 5.2 7 13 7 13s7-7.8 7-13a7 7 0 0 0-7-7zm0 9.5A2.5 2.5 0 1 1 12 6.5a2.5 2.5 0 0 1 0 5z"/></svg>
        <span>123 Name Street, 000<br>Your City, 00000-000</span>
      </li>
    </ul>
  </section>

  <section class="card card-back">
    <div class="brand">
      <div class="brand-row">
        <span class="brand-square"></span>
        <span class="brand-name">Varek Services</span>
      </div>
      <p class="brand-slogan">• From lodges to landmarks •</p>
    </div>
  </section>

</body>
</html>
```